Brava Stone Oven Kitchen (restaurant)

Restaurant with a cool vibe.
We need a refresh of existing site. Appealing to a hip crowd of 25 or older age bracket (mid price to high small town). Constant changes food and cocktail menu. A vibing atmosphere with jazz funk hip music.
Must be able to scale for any device… phone/mobile device super important.
Instagram: @Brava.Linwell
Website: bravalinwell.example

Target Market(s)

25-55 age group

Number of Pages Required

1 page

Font styles to use
Sans Serif

Requirements
Must have
• Simple to navigate. Simplicity is the key to all sophistication.

Links/Buttons
Menu
Gift Cards
Reservations
Take Out
Contact Us
Should not have
• Please, nothing generic looking… no cookie cutter look. Originality

```html
<!DOCTYPE html>
<html lang="en">
<head>
<meta charset="utf-8">
<title>Brava Stone Oven Kitchen</title>
<link rel="stylesheet" href="https://fonts.googleapis.com/css2?family=Poppins:ital,wght@0,400;0,500;0,600;0,700;1,400&display=swap">
<style>
:root{
  --yellow:#f2c40f;
  --black:#111111;
  --dark:#1d1d1d;
  --footer:#333333;
  --white:#ffffff;
  --grey:#f6f6f8;
  --text:#222222;
  --muted:#555555;
}
*{margin:0;padding:0;box-sizing:border-box}
html,body{width:1200px;height:3583px;overflow:hidden}
body{background:var(--yellow);font-family:'Poppins',sans-serif;color:var(--text);position:relative}
.page{position:absolute;left:95px;top:104px;width:1009px;height:3364px;background:var(--white);box-shadow:0 10px 30px rgba(0,0,0,.25);overflow:hidden}
.abs{position:absolute}
.btn{position:absolute;display:flex;align-items:center;justify-content:center;border-radius:20px;font-weight:600;font-size:12px}
.btn-yellow{background:var(--yellow);color:var(--black)}
.btn-outline{border:1px solid var(--yellow);color:var(--yellow)}
/* nav */
.nav{left:0;top:0;width:1009px;height:53px;background:var(--black)}
.nav-tab{left:136px;top:20px;width:126px;height:60px;background:var(--black);border-radius:0 0 63px 63px}
.brand{color:var(--white);font-weight:700;line-height:1}
.nav .brand{left:169px;top:12px;font-size:15px;width:160px}
.nav .brand small{display:block;font-size:8px;font-weight:700;margin-top:2px}
.nav-link{top:19px;color:var(--white);font-size:10px}
/* hero */
.hero{left:0;top:53px;width:1009px;height:424px;background:linear-gradient(135deg,#3a2e2a 0%,#4a3a32 40%,#2f2d30 70%,#3d3a3a 100%)}
.hero-title{left:0;width:1009px;top:140px;text-align:center;font-size:40px;font-weight:600;line-height:47px;color:var(--white)}
.hero-title span{color:var(--yellow)}
/* features */
.feature{width:180px;height:180px;border-radius:50%;border:4px solid var(--yellow);display:flex;flex-direction:column;align-items:center;justify-content:center;text-align:center}
.feature.black{background:var(--black);color:var(--white)}
.feature.yellow{background:var(--yellow);color:var(--black)}
.feature h3{font-size:13px;font-weight:700;margin:10px 0 8px}
.feature p{font-size:8px;line-height:10px;width:100px}
/* about */
.photo-main{left:169px;top:798px;width:306px;height:196px;background:linear-gradient(135deg,#5a3a22,#2a1d16 60%,#6b4a33)}
.photo-small{left:379px;top:933px;width:167px;height:96px;background:linear-gradient(180deg,#7c8fa8,#7a4a38 50%,#4a3024);border:5px solid var(--white);box-shadow:0 2px 8px rgba(0,0,0,.3)}
.about h2{font-size:18px;font-weight:600}
.about p{font-size:9px;line-height:10.5px;color:var(--text);width:255px;margin-top:14px}
/* menu */
.menu-band{left:-240px;top:1089px;width:1489px;height:811px;border-radius:50%;background:var(--dark)}
.menu-title{left:0;width:1009px;top:1172px;text-align:center;color:var(--white);font-size:18px;font-weight:500}
.tab{position:absolute;top:1246px;height:36px;width:123px;border-radius:20px;display:flex;align-items:center;justify-content:center;gap:10px;font-size:13px}
.tab.active{background:var(--yellow);color:var(--white)}
.tab.idle{border:1px solid #777;color:var(--white);background:var(--black)}
.dish{position:absolute;width:211px;height:179px;border:1px solid #a58814;display:flex;flex-direction:column;align-items:center;justify-content:center;gap:22px}
.dish h4{color:var(--white);font-size:13px;font-weight:700}
.dish .btn{position:static;width:80px;height:25px;font-size:9px}
.dish.g1{background:linear-gradient(135deg,#3b2a1e,#1d1a17)}
.dish.g2{background:linear-gradient(135deg,#2d2520,#3a2a1c)}
.dish.g3{background:linear-gradient(135deg,#1d2a1d,#2a1f1a)}
.dish.g4{background:linear-gradient(135deg,#2f2418,#1e1b18)}
.dish.g5{background:linear-gradient(135deg,#3b2a1e,#4a2a18)}
.dish.g6{background:linear-gradient(135deg,#241c16,#3a2a1e)}
/* specials */
.section-title{left:0;width:1009px;text-align:center;font-size:19px;font-weight:500;color:var(--black)}
.special-img{position:absolute;top:2038px;width:212px;height:179px}
.special h5{position:absolute;top:2233px;font-size:10px;font-weight:700}
.special p{position:absolute;top:2258px;font-size:8px;line-height:10px;width:140px;color:var(--muted)}
/* reservations */
.reserve{left:169px;top:2352px;width:671px;height:241px;background:var(--yellow);border-radius:4px}
.reserve h2{position:absolute;top:32px;width:100%;text-align:center;font-size:19px;font-weight:600}
.field{position:absolute;background:var(--grey);height:27px;font-size:8px;padding:9px 0 0 22px;color:#444}
/* testimonials */
.quote-card{left:305px;top:2783px;width:408px;height:279px;background:var(--grey)}
.avatar{position:absolute;border-radius:50%;border:3px solid var(--yellow)}
.rating{position:absolute;width:44px;height:44px;border-radius:50%;background:var(--white);box-shadow:0 0 6px rgba(0,0,0,.08);display:flex;align-items:center;justify-content:center;font-size:9px;color:var(--yellow)}
.quote{left:305px;top:2880px;width:408px;text-align:center;font-style:italic;font-size:12px;line-height:25.5px;color:#555}
.dot{position:absolute;top:3022px;width:9px;height:9px;border-radius:50%;background:#f1a6b6}
/* footer */
.footer{left:0;top:3125px;width:1009px;height:239px;background:var(--footer);color:var(--white)}
.footer .brand{left:169px;top:46px;font-size:26px}
.footer .brand small{display:block;font-size:9px;margin-top:2px}
.foot-link{top:63px;font-size:10px}
.info{top:123px;font-size:8.5px;line-height:10px;display:flex;gap:8px}
.info b{display:block;font-weight:400;margin-bottom:2px}
.rule{left:169px;top:169px;width:671px;height:1px;background:#555}
</style>
</head>
<body>
<div class="page">
  <!-- navigation -->
  <div class="abs nav-tab"></div>
  <header class="abs nav">
    <div class="abs brand">BRAVA<small>Stone Oven Kitchen</small></div>
    <span class="abs nav-link" style="left:396px">Home</span>
    <span class="abs nav-link" style="left:458px">Menu</span>
    <span class="abs nav-link" style="left:519px">Reservations</span>
    <span class="abs nav-link" style="left:605px">Order Online</span>
    <span class="abs nav-link" style="left:699px">About Us</span>
    <span class="btn btn-yellow" style="left:757px;top:17px;width:83px;height:25px;font-size:10px">Contact Us</span>
  </header>

  <!-- hero -->
  <section class="abs hero" role="img" aria-label="Photo of the restaurant's brick building front"></section>
  <h1 class="abs hero-title"><span>Dinner Ideas?</span> How<br>About Brava!</h1>
  <span class="btn btn-yellow" style="left:475px;top:328px;width:103px;height:28px">Book Now</span>

  <!-- features -->
  <div class="abs feature black" style="left:169px;top:547px">
    <svg width="30" height="30" viewBox="0 0 30 30" fill="none" stroke="#fff" stroke-width="2"><rect x="5" y="5" width="20" height="14" rx="1"/><path d="M2 24h26M11 12l3 3 5-6"/></svg>
    <h3>Order Online</h3><p>Lorem ipsum is simply dummy text</p>
  </div>
  <div class="abs feature yellow" style="left:414px;top:547px">
    <svg width="34" height="34" viewBox="0 0 34 34" fill="none" stroke="#111" stroke-width="2"><circle cx="16" cy="7" r="3"/><path d="M16 11v10h6v8M6 22h14M8 22v8M18 22v8M26 8a4 4 0 1 0 .1 0"/></svg>
    <h3>Book A Table</h3><p>Lorem ipsum is simply dummy text</p>
  </div>
  <div class="abs feature black" style="left:662px;top:547px">
    <svg width="34" height="34" viewBox="0 0 34 34" fill="none" stroke="#fff" stroke-width="2"><circle cx="17" cy="17" r="13"/><text x="17" y="21" fill="#fff" stroke="none" font-size="11" font-weight="700" text-anchor="middle" font-family="Poppins,sans-serif">24</text></svg>
    <h3>Hours &amp; Contact</h3><p>Lorem ipsum is simply dummy text</p>
  </div>

  <!-- about -->
  <div class="abs photo-main" role="img" aria-label="Photo of the owners inside the restaurant"></div>
  <div class="abs photo-small" role="img" aria-label="Photo of the restaurant building"></div>
  <div class="abs about" style="left:586px;top:805px">
    <h2>About</h2>
    <p>Lorem Ipsum is simply dummy text of the printing and typesetting industry. Lorem Ipsum has been the industry's standard dummy text ever since the 1500s, when an unknown printer took a galley</p>
    <p style="margin-top:12px">It is a long established fact that a reader will be distracted by the readable content of a page when looking at its layout. The point of using Lorem Ipsum is that it has a more-or-less norma</p>
  </div>
  <span class="btn btn-yellow" style="left:586px;top:966px;width:105px;height:28px;font-size:12px">Read More</span>

  <!-- menu -->
  <div class="abs menu-band"></div>
  <h2 class="abs menu-title">From Our Menu</h2>
  <div class="tab active" style="left:376px">
    <svg width="16" height="14" viewBox="0 0 16 14" fill="#fff"><path d="M1 11h14v2H1zM2 10a6 6 0 0 1 12 0z"/></svg>Dinner</div>
  <div class="tab idle" style="left:512px">
    <svg width="16" height="14" viewBox="0 0 16 14" fill="#fff"><path d="M1 8h14l-2 5H3zM4 6a4 3 0 0 1 8 0z"/></svg>Take Out</div>

  <div class="dish g1" style="left:168px;top:1357px" role="img" aria-label="Shareable plates photo"><h4>Shareable</h4><span class="btn btn-yellow">View More</span></div>
  <div class="dish g2" style="left:397px;top:1357px" role="img" aria-label="Wood fired pizza photo"><h4>Wood Fired Pizaa</h4><span class="btn btn-outline">View More</span></div>
  <div class="dish g3" style="left:626px;top:1357px" role="img" aria-label="Salad photo"><h4>Salads</h4><span class="btn btn-outline">View More</span></div>
  <div class="dish g4" style="left:168px;top:1556px" role="img" aria-label="Sandwich photo"><h4>Sandwixhes</h4><span class="btn btn-outline">View More</span></div>
  <div class="dish g5" style="left:397px;top:1556px" role="img" aria-label="Pasta photo"><h4>Mains &amp; Pasta</h4><span class="btn btn-outline">View More</span></div>
  <div class="dish g6" style="left:626px;top:1556px" role="img" aria-label="Burger photo"><h4>Burgers</h4><span class="btn btn-outline">View More</span></div>
  <span class="abs" style="left:0;width:1009px;top:1792px;text-align:center;color:#fff;font-size:10px;font-weight:600">View More</span>

  <!-- specials -->
  <h2 class="abs section-title" style="top:1960px">This Week Special Food</h2>
  <div class="special">
    <div class="special-img" style="left:169px;background:linear-gradient(135deg,#2a2420,#c2541c 60%,#3a2a20)" role="img" aria-label="Lentil curry dish photo"></div>
    <div class="special-img" style="left:397px;background:linear-gradient(135deg,#8a8a88,#d08a2a 50%,#2a2a2a)" role="img" aria-label="Chicken curry dish photo"></div>
    <div class="special-img" style="left:628px;background:linear-gradient(135deg,#d8631a,#e9a13a 50%,#7a3a1c)" role="img" aria-label="Dal soup dish photo"></div>
    <h5 style="left:169px">stablished fact that a reader</h5>
    <h5 style="left:395px">stablished fact that a reader</h5>
    <h5 style="left:626px">stablished fact that a reader</h5>
    <p style="left:169px">It is a long established fact that a reader will be distracted by the readable content</p>
    <p style="left:395px">It is a long established fact that a reader will be distracted by the readable content</p>
    <p style="left:626px">It is a long established fact that a reader will be distracted by the readable content</p>
  </div>

  <!-- reservations -->
  <section class="abs reserve">
    <h2>Reservations</h2>
    <div class="field" style="left:156px;top:86px;width:174px">Date</div>
    <div class="field" style="left:341px;top:86px;width:175px">Time</div>
    <div class="field" style="left:156px;top:128px;width:360px">Party Size</div>
    <span class="btn" style="left:288px;top:178px;width:96px;height:28px;background:var(--black);color:#fff;font-size:9px">Send Now</span>
  </section>

  <!-- testimonials -->
  <h2 class="abs section-title" style="top:2653px">Client Are Saying</h2>
  <div class="abs quote-card"></div>
  <div class="avatar" style="left:464px;top:2735px;width:88px;height:88px;background:#c9c9cc" role="img" aria-label="Portrait of Jalen Mercer"></div>
  <div class="avatar" style="left:182px;top:2890px;width:90px;height:90px;background:#e6dcd4" role="img" aria-label="Portrait of a smiling guest"></div>
  <div class="avatar" style="left:745px;top:2890px;width:90px;height:90px;background:#e47aa6" role="img" aria-label="Portrait of a guest in pink"></div>
  <div class="rating" style="left:689px;top:2760px">5★</div>
  <div class="rating" style="left:172px;top:2868px">5★</div>
  <div class="rating" style="left:798px;top:2868px">5★</div>
  <h3 class="abs" style="left:305px;width:408px;top:2836px;text-align:center;font-size:16px;font-weight:500">Jalen Mercer</h3>
  <p class="abs quote">Lorem Ipsum is simply dummy text of the printing<br>and typesetting industry. Lorem Ipsum has been<br>the industry's standard dummy text ever since the<br>1500s, when an unknown printer took a galley</p>
  <span class="dot" style="left:494px"></span>
  <span class="dot" style="left:505px;background:var(--yellow);width:10px;height:10px;top:3021px"></span>
  <span class="dot" style="left:517px;background:#f1a6e6"></span>
  <span class="dot" style="left:528px"></span>

  <!-- footer -->
  <footer class="abs footer">
    <div class="abs brand">BRAVA<small>Stone Oven Kitchen</small></div>
    <span class="abs foot-link" style="left:482px">Home</span>
    <span class="abs foot-link" style="left:537px">What We Do</span>
    <span class="abs foot-link" style="left:620px">Who We Are</span>
    <span class="abs foot-link" style="left:704px">Testimonial</span>
    <span class="abs foot-link" style="left:786px">Contact US</span>
    <div class="abs info" style="left:169px">
      <svg width="18" height="22" viewBox="0 0 18 22" fill="none" stroke="#f2c40f" stroke-width="1.5"><path d="M9 21s7-7 7-12A7 7 0 0 0 2 9c0 5 7 12 7 12z"/><circle cx="9" cy="9" r="2.5"/></svg>
      <div><b>Address</b>PO Box 48, Fernway St,<br>Linwell 4021</div>
    </div>
    <div class="abs info" style="left:350px">
      <svg width="20" height="20" viewBox="0 0 20 20" fill="none" stroke="#f2c40f" stroke-width="1.5"><path d="M4 2l4 4-2 2c1 3 3 5 6 6l2-2 4 4-3 3C8 18 2 12 1 5z"/></svg>
      <div><b>Call Us Now</b>(0000)-000-000</div>
    </div>
    <div class="abs info" style="left:516px">
      <svg width="20" height="20" viewBox="0 0 20 20" fill="none" stroke="#f2c40f" stroke-width="1.5"><rect x="2" y="5" width="16" height="12"/><path d="M2 5l8 6 8-6"/></svg>
      <div><b>Mail Id</b>info@bravalinwell.example</div>
    </div>
    <div class="abs" style="left:700px;top:120px;font-size:9px">Subscribe Newsletter</div>
    <div class="abs" style="left:701px;top:135px;width:110px;height:20px;background:#fff;color:#333;font-size:7.5px;padding:5px 6px">Enter Email ID</div>
    <div class="abs" style="left:815px;top:135px;width:25px;height:20px;background:var(--yellow);display:flex;align-items:center;justify-content:center">
      <svg width="11" height="11" viewBox="0 0 12 12" fill="#fff"><path d="M1 6l10-5-3 10-2-4z"/></svg>
    </div>
    <div class="abs rule"></div>
    <div class="abs" style="left:0;width:1009px;top:187px;text-align:center;font-size:8.5px">© 2021 Brava</div>
  </footer>
</div>
</body>
</html>
```